Highlight Document Over Image for Slide

We are seeking a graphic designer to overlay a news article on an image that pertains to the article, aiming for a stylish yet professional appearance. Given the limited resources, we encourage you to use your imagination and go beyond what basic tools like PowerPoint can offer.

```html
<!DOCTYPE html>
<html lang="en">
<head>
<meta charset="UTF-8">
<title>Contraband Rule Highlight</title>
<link href="https://fonts.googleapis.com/css2?family=Tinos:wght@400;700&display=swap" rel="stylesheet">
<style>
  :root {
    --land: #8a7f6c;
    --land-dark: #5d584e;
    --water: #4b4a47;
    --water-deep: #3f3e3b;
    --card-dark: #3b3b3b;
    --card-mid: #555;
    --paper: #efece4;
    --paper-shade: #e2ded3;
    --ink: #2a2a2a;
    --heading-line: #f0a45a;
    --highlight: #f5a9b8;
    --pin: #d81414;
    --pin-dark: #8c0a0a;
    --sign: #d62a2a;
  }
  * { margin: 0; padding: 0; box-sizing: border-box; }
  html, body { width: 1200px; height: 857px; overflow: hidden; }
  body { position: relative; font-family: "Tinos", "Times New Roman", serif; background: var(--water); }

  .aerial-backdrop {
    position: absolute; inset: 0;
    background:
      linear-gradient(150deg, var(--land) 0%, var(--land-dark) 30%, transparent 48%),
      linear-gradient(200deg, #7e7668 0%, transparent 28%),
      linear-gradient(160deg, var(--water) 50%, var(--water-deep) 100%);
  }

  .rule-card {
    position: absolute; left: 407px; top: 197px;
    width: 580px; height: 475px;
    background: linear-gradient(180deg, var(--card-dark), var(--card-mid) 8%, var(--card-dark) 14%, var(--card-dark) 88%, var(--card-mid) 94%, var(--card-dark));
    filter: drop-shadow(0 10px 14px rgba(0,0,0,.55));
  }
  .rule-paper {
    position: absolute; left: 0; top: 16px; width: 580px; height: 432px;
    background: radial-gradient(ellipse at 50% 45%, var(--paper) 60%, var(--paper-shade) 100%);
    clip-path: polygon(0 2%, 6% 0.5%, 12% 2.5%, 20% 0.8%, 28% 2.2%, 35% 0.4%, 44% 2%, 52% 0.6%, 61% 2.4%, 70% 0.7%, 78% 2%, 86% 0.5%, 93% 2.2%, 100% 1%,
      99.4% 20%, 100% 45%, 99.5% 75%, 100% 98.5%,
      94% 99.5%, 87% 97.6%, 79% 99.6%, 71% 97.8%, 63% 99.4%, 55% 97.5%, 47% 99.5%, 39% 97.7%, 30% 99.6%, 22% 97.8%, 14% 99.3%, 7% 97.6%, 0 99.2%,
      0.6% 70%, 0 40%, 0.5% 15%);
  }

  .push-pin { position: absolute; left: 282px; top: -12px; width: 52px; height: 52px; }

  .rule-heading {
    position: absolute; left: 48px; top: 66px; width: 400px;
    display: flex; gap: 6px;
    font-weight: 700; font-size: 18px; line-height: 20px; color: var(--ink);
  }
  .rule-number { padding-left: 12px; }
  .rule-title { text-decoration: underline; text-decoration-color: var(--ink); text-underline-offset: 3px; }
  .rule-title-underline { position: absolute; left: 24px; top: 44px; width: 303px; height: 3px; background: var(--heading-line); }
  .prohibited-icon { position: absolute; left: -7px; top: 6px; width: 48px; height: 48px; }

  .rule-body {
    position: absolute; left: 89px; top: 110px; width: 410px;
    font-size: 19px; line-height: 23.5px; color: var(--ink);
    text-align: justify;
  }
  .mark { background: var(--highlight); border-radius: 6px; padding: 1px 2px; box-decoration-break: clone; -webkit-box-decoration-break: clone; }
  .page-number { position: absolute; left: 0; right: 0; top: 406px; text-align: center; font-size: 17px; color: #555; font-family: "Tinos", serif; }
</style>
</head>
<body>
  <div class="aerial-backdrop" role="img" aria-label="Aerial map of a waterfront correctional facility, its streets and the bay shoreline"></div>

  <div class="rule-card">
    <div class="rule-paper">
      <div class="rule-heading">
        <svg class="prohibited-icon" viewBox="0 0 48 48" aria-hidden="true">
          <rect x="11" y="22" width="26" height="5" fill="none" stroke="var(--sign)" stroke-width="1.5"/>
          <line x1="32" y1="22" x2="32" y2="27" stroke="var(--sign)" stroke-width="1.5"/>
          <circle cx="24" cy="24" r="19" fill="none" stroke="var(--sign)" stroke-width="3.5"/>
          <line x1="11" y1="11" x2="37" y2="37" stroke="var(--sign)" stroke-width="3.5"/>
        </svg>
        <span class="rule-number">20.</span>
        <span class="rule-title">INTRODUCTION OR POSSESSION OF CONTRABAND ITEMS</span>
      </div>
      <p class="rule-body">
        Employees shall not introduce or possess unauthorized items such as <span class="mark">escape paraphernalia, weapons, facsimiles of weapons, ammunition, wireless communication devices, cell phones, tobacco or facsimiles of tobacco products (e.g. electronic vapor cigarettes), lighters or any other item</span> not specifically authorized by PD 04.04.100 "Custody, Security and Safety Systems (Exempt)", OP 04.04.100 "Gate Security" or facility operating procedure in any facility where offenders are housed. Employees are responsible for any item in their
      </p>
      <div class="page-number">36</div>
    </div>
    <svg class="push-pin" viewBox="0 0 52 52" aria-hidden="true">
      <defs>
        <radialGradient id="pinHead" cx="35%" cy="30%" r="70%">
          <stop offset="0" stop-color="#ff6b6b"/>
          <stop offset=".45" stop-color="var(--pin)"/>
          <stop offset="1" stop-color="var(--pin-dark)"/>
        </radialGradient>
      </defs>
      <ellipse cx="20" cy="40" rx="14" ry="5" fill="rgba(0,0,0,.35)"/>
      <line x1="22" y1="30" x2="14" y2="42" stroke="#999" stroke-width="2"/>
      <ellipse cx="24" cy="30" rx="13" ry="7" fill="var(--pin-dark)"/>
      <circle cx="29" cy="20" r="14" fill="url(#pinHead)"/>
    </svg>
  </div>
</body>
</html>
```